Accounting business needs a great flyer

I need a flyer for my new business "Ledgerline". I am an individual accountant working for himself on the Sunshine Coast in Queensland Australia. I would like to see designs that communicate reliability and trust. I believe my point of difference is that I am always available to my clients and I will cap my number of clients to ensure I can service them properly.
The main point I want to convey is that most of the time junior employees with little to no experience or unqualified employees do the tax work for the clients and a senior accountant quickly checks the work at the end but never gets to really know the clients business. Accountants in general seem to have a bad reputation for not responding to clients in a timely fashion, whether by email or phone. This is where I intend to differentiate myself. . I have also included some logo's that should go on the flyer.

Target Market(s)

Every small business

Industry/Entity Type

Public Accounting

Requirements
Must have
• Web address: www.ledgerline.com.au
Phone number: 0417 582 396
Attached logos
Reference to: "Do you know who is actually doing your tax?"
Other accounting firms - use junior unqualified staff
- outsource to cheap labour countries
- use tax consultants who sometimes have had only 2 weeks training.
At Ledgerline, a highly qualified CPA with a Masters in Taxation does your work from start to finish.
**I don't need it to say exactly this but I want the theme of the flyer to have these points in it.
Nice to have
• Something different

```html
<!DOCTYPE html>
<html lang="en">
<head>
<meta charset="utf-8">
<title>Ledgerline – Flyer</title>
<link rel="stylesheet" href="https://fonts.googleapis.com/css2?family=Roboto+Condensed:ital,wght@0,400;0,700;1,400&family=Montserrat:wght@500&display=swap">
<style>
  :root {
    --backdrop: #e4e4e4;
    --paper: #ffffff;
    --paper-shade: #ececec;
    --ink: #2b2b2b;
    --ink-soft: #3a3a3a;
    --band: #2a2d2e;
    --band-edge: #9a9a9a;
    --photo-warm: #e8d9c4;
    --photo-desk: #8a6a4e;
    --photo-paper: #c9ccd2;
    --photo-suit: #23262b;
    --badge-blue: #27b6e8;
    --badge-navy: #1d5fa8;
    --badge-grey: #d8d8d8;
    --white: #ffffff;
  }
  * { margin: 0; padding: 0; box-sizing: border-box; }
  html, body {
    width: 1045px;
    height: 1200px;
    overflow: hidden;
    background: var(--backdrop);
  }
  .flyer {
    position: absolute;
    left: 112px;
    top: 20px;
    width: 767px;
    height: 1085px;
    transform: scale(1.07);
    transform-origin: 0 0;
    background: linear-gradient(100deg, var(--paper-shade) 0%, var(--paper) 40%, var(--paper) 100%);
    overflow: hidden;
    font-family: "Roboto Condensed", "Arial Narrow", sans-serif;
    color: var(--ink);
    box-shadow: 0 12px 24px rgba(0,0,0,0.18);
  }
  .flyer__shapes {
    position: absolute;
    inset: 0;
    width: 767px;
    height: 1085px;
  }
  .brand {
    position: absolute;
    left: 0;
    width: 767px;
    top: 505px;
    text-align: center;
    font-family: "Montserrat", sans-serif;
    font-weight: 500;
    font-size: 38px;
    letter-spacing: 14px;
    padding-left: 14px;
    color: var(--ink);
  }
  .pitch {
    position: absolute;
    left: 120px;
    top: 580px;
    width: 580px;
  }
  .pitch__question {
    font-weight: 700;
    font-size: 23px;
    line-height: 30px;
  }
  .pitch__lead {
    font-style: italic;
    font-size: 19px;
    line-height: 24px;
    color: var(--ink-soft);
  }
  .pitch__list { list-style: none; margin-top: 4px; }
  .pitch__item {
    display: flex;
    align-items: center;
    gap: 8px;
    font-size: 19px;
    line-height: 24px;
    color: var(--ink-soft);
  }
  .pitch__icon { width: 16px; height: 16px; flex: none; }
  .promise {
    position: absolute;
    left: 0;
    width: 767px;
    top: 712px;
    text-align: center;
    font-weight: 700;
    font-size: 33px;
    line-height: 37px;
    text-transform: uppercase;
    color: var(--ink);
  }
  .contact {
    position: absolute;
    left: 0;
    width: 767px;
    top: 1012px;
    text-align: center;
    font-weight: 700;
    font-size: 44px;
    color: var(--white);
    letter-spacing: 0.5px;
  }
</style>
</head>
<body>
<main class="flyer">
  <svg class="flyer__shapes" viewBox="0 0 767 1085">
    <defs>
      <linearGradient id="photoBase" x1="0" y1="0" x2="1" y2="0.6">
        <stop offset="0" stop-color="#6b625a"/>
        <stop offset="0.45" stop-color="var(--photo-desk)"/>
        <stop offset="0.75" stop-color="#3a3c42"/>
        <stop offset="1" stop-color="var(--photo-suit)"/>
      </linearGradient>
      <radialGradient id="photoGlow" cx="0.3" cy="0.05" r="0.45">
        <stop offset="0" stop-color="var(--photo-warm)" stop-opacity="0.95"/>
        <stop offset="1" stop-color="var(--photo-warm)" stop-opacity="0"/>
      </radialGradient>
      <radialGradient id="photoPaper" cx="0.62" cy="0.78" r="0.38">
        <stop offset="0" stop-color="var(--photo-paper)" stop-opacity="0.9"/>
        <stop offset="1" stop-color="var(--photo-paper)" stop-opacity="0"/>
      </radialGradient>
      <linearGradient id="photoShade" x1="0" y1="0" x2="0" y2="1">
        <stop offset="0" stop-color="#1c1e22" stop-opacity="0.55"/>
        <stop offset="0.35" stop-color="#1c1e22" stop-opacity="0"/>
      </linearGradient>
      <clipPath id="headerClip">
        <path d="M0,0 L767,0 L767,255 Q640,420 420,438 Q150,440 0,170 Z"/>
      </clipPath>
    </defs>

    <path class="header-rim" d="M420,438 Q640,420 767,255 L767,272 Q650,442 420,446 Z" fill="var(--band)"/>

    <g class="header-photo" role="img" aria-label="Photograph of business people reviewing financial charts with pens beside a laptop" clip-path="url(#headerClip)">
      <rect width="767" height="450" fill="url(#photoBase)"/>
      <rect width="767" height="450" fill="url(#photoPaper)"/>
      <rect width="767" height="450" fill="url(#photoGlow)"/>
      <rect x="380" width="387" height="450" fill="url(#photoShade)"/>
    </g>

    <circle class="brand-seal" cx="383" cy="432" r="66" fill="var(--white)" stroke="var(--ink)" stroke-width="3"/>

    <path class="footer-edge" d="M0,808 Q383,1190 767,820 L767,830 Q383,1192 0,820 Z" fill="var(--band-edge)"/>
    <path class="footer-band" d="M0,820 Q383,1192 767,830 L767,1085 L0,1085 Z" fill="var(--band)"/>

    <circle class="badge badge--software" cx="238" cy="897" r="40" fill="var(--badge-blue)"/>
    <rect class="badge badge--institute" x="296" y="860" width="173" height="75" fill="var(--badge-navy)"/>
    <circle class="badge badge--registry" cx="528" cy="897" r="40" fill="var(--badge-grey)"/>
  </svg>

  <div class="brand">LEDGERLINE</div>

  <section class="pitch">
    <p class="pitch__question">Do you know who is actually doing your tax?</p>
    <p class="pitch__lead">Other accounting firms - use junior unqualified staff</p>
    <ul class="pitch__list">
      <li class="pitch__item">
        <svg class="pitch__icon" viewBox="0 0 16 16"><circle cx="8" cy="8" r="8" fill="var(--ink)"/><path d="M5,5 L11,11 M11,5 L5,11" stroke="var(--white)" stroke-width="2"/></svg>
        Outsource to cheap labour countries
      </li>
      <li class="pitch__item">
        <svg class="pitch__icon" viewBox="0 0 16 16"><circle cx="8" cy="8" r="8" fill="var(--ink)"/><path d="M5,5 L11,11 M11,5 L5,11" stroke="var(--white)" stroke-width="2"/></svg>
        Use tax consultants who sometimes have had only 2 weeks training.
      </li>
    </ul>
  </section>

  <p class="promise">At Ledgerline, a highly qualified<br>CPA with a Masters in Taxation does<br>your work from start to finish.</p>

  <p class="contact">0417 582 396 &nbsp;|&nbsp; LEDGERLINE.COM.AU</p>
</main>
</body>
</html>
```